Corporate Identity Pack - LetterHead, Business Card, Envelope

We are looking for a clean, professional, and visually connected corporate identity set for our company "VELTA HOME" (Cleaning, Gardening, and Pest Control services).

The pack must include:

Business Card (front and back)
Envelope with recipient window on the right side (22x11)
A4 Letterhead

We provide:
Our final logo (PNG)
Three design references (Inspiration1, Inspiration2, Inspiration3) to spark ideas — but you are absolutely free to propose your own creative solutions based on these concepts.

What we want:
A clean, modern, and trustworthy style
A subtle but creative watermark or graphic detail on the letterhead (not too invasive)

The same visual "family feeling" across business card, envelope, and letterhead: designs must be different but clearly connected

Strong readability for all text and contact details

Use our brand colors (Navy Blue, Green, Orange/Red) in a smart, non-overloaded way

No strict limitations: we are open to creative proposals as long as they are coherent, elegant, and suitable for professional use

Technical specifications:
100% full A4 page layout (no accidental borders)

Deliver ready-to-print PDFs and vector files (AI, EPS)

Respect 5 mm safety margins

Standard sizes for A4, business card, envelope C6 with window at the right

Tone:
Modern – Clean – Elegant – Creative – Trustworthy

Target Market(s)

Professional businesses, property managers, condominium administrators, companies, clinics, and offices requiring cleaning, gardening, and pest control services. The design must convey trust, reliability, professionalism, and attention to detail.

Industry/Entity Type

Cleaning Services, Gardening Services, Pest Control Services

Colors
0054AA
0677BA
7BADD7
CADEEF
E8F1F8
59FF00
82FF00
B8FF75
E3FFCB
F4FFEA
EB3D1F
EC4F4E
F09395
F8D3D4
FCEDEE

Requirements
Must have
• Cohesive design across business card, letterhead, and envelope Clean, modern, professional look Use of brand colors: Navy Blue (main), Green, Orange/Red accents Letterhead must include a subtle watermark without interfering with text Envelope must be with a transparent window for recipient address visibility High readability of all text and contact details Proper alignment, no unnecessary margins (full A4 layout)
Nice to have
• Creative but discreet use of the checkmark from the logo as part of the background or watermark Slight variation or accent of color tones while respecting brand identity A clean visual accent that gives a sense of movement or dynamic professionalism (without being distracting) Icons for email, phone, and website on the business card (if stylistically appropriate)
Should not have
• Overuse of colors or rainbow effects Heavy backgrounds or complex textures that interfere with readability Fonts that are too playful, comic-style, or non-professional Overcrowded layouts — the design must feel clean and spacious Watermarks that are too strong or central (they must be subtle and marginal)

```html
<!DOCTYPE html>
<html lang="en">
<head>
<meta charset="utf-8">
<title>VELTA HOME – Business Card</title>
<link href="https://fonts.googleapis.com/css2?family=Montserrat:wght@400;600;700&family=Arimo:wght@400;700&display=swap" rel="stylesheet">
<style>
  :root{
    --bg:#3c3c3c;
    --card-dark:#333333;
    --card-light:#ffffff;
    --navy:#14137a;
    --navy-on-dark:#5a6cf0;
    --green:#5fd12a;
    --orange:#f06a12;
    --ink-light:#f2f2f2;
  }
  *{box-sizing:border-box;margin:0;padding:0}
  html,body{width:1200px;height:803px;overflow:hidden;background:var(--bg)}
  .canvas{position:relative;width:1200px;height:803px;display:flex;align-items:center;justify-content:center;gap:60px}
  .card{position:relative;width:510px;height:330px;border-radius:18px;overflow:hidden;border-bottom:4px solid var(--green);border-left:2px solid var(--green);box-shadow:0 18px 40px rgba(0,0,0,.45)}
  .card--back{background:var(--card-dark);display:flex}
  .card--front{background:var(--card-light);display:flex;align-items:center;justify-content:center}

  .back-info{width:58%;padding:28px 0 0 30px;font-family:"Arimo",sans-serif;color:var(--ink-light)}
  .brand{display:flex;align-items:center;gap:8px;font-family:"Montserrat",sans-serif;font-weight:700;color:var(--navy);white-space:nowrap}
  .brand__mark{width:14px;height:14px;background:var(--navy)}
  .brand--small{font-size:20px;letter-spacing:.5px;color:var(--navy-on-dark)}
  .brand--small .brand__mark{background:var(--navy-on-dark)}
  .person__name{margin-top:14px;font-family:"Montserrat",sans-serif;font-weight:700;font-size:20px;line-height:1.2;color:var(--navy-on-dark);letter-spacing:.5px}
  .person__role{font-size:13px;line-height:1.3;color:var(--green);margin-top:2px}
  .address{margin-top:11px;font-size:13px;line-height:1.32}
  .contacts{margin-top:9px;list-style:none;font-size:13px;line-height:1.38}
  .contacts li{display:flex;align-items:center;gap:8px;white-space:nowrap}
  .contacts svg{width:12px;height:12px;flex:none}
  .back-panel{flex:1;margin:22px 22px 22px 0;border-radius:6px;background:linear-gradient(135deg,#2e2e2e,#4a4a4a)}

  .brand--large{font-size:44px;letter-spacing:1px;gap:14px}
  .brand--large .brand__mark{width:30px;height:30px}
</style>
</head>
<body>
<main class="canvas">
  <section class="card card--back" aria-label="Business card back">
    <div class="back-info">
      <div class="brand brand--small"><span class="brand__mark"></span>VELTA HOME</div>
      <p class="person__name">MARCO REITER</p>
      <p class="person__role">President</p>
      <p class="address">Via dei Pini 24 - Kiefernweg 24<br>I-39100 Valdora-Walden (Bz)<br>REA-VWV Nr. Bz 517302<br>P.I.-MwSt. 04518830264</p>
      <ul class="contacts">
        <li><svg viewBox="0 0 12 12"><path d="M3 1l2 2-1 1.5c.6 1.4 1.6 2.4 3 3L8.5 6.5l2 2L9 10.5C5 10 2 7 1.5 3z" fill="var(--orange)"/></svg>+39 345 1209874</li>
        <li><svg viewBox="0 0 12 12"><rect x="1" y="2.5" width="10" height="7" fill="var(--orange)"/><path d="M1 2.5l5 4 5-4" stroke="var(--card-dark)" fill="none"/></svg>office@veltahome.example</li>
        <li><svg viewBox="0 0 12 12"><circle cx="6" cy="6" r="5" fill="var(--orange)"/><path d="M1 6h10M6 1c-2 3-2 7 0 10M6 1c2 3 2 7 0 10" stroke="var(--card-dark)" fill="none" stroke-width=".8"/></svg>www.veltahome.example</li>
        <li><svg viewBox="0 0 12 12"><rect x="1" y="3" width="10" height="6" rx="2" fill="none" stroke="var(--navy-on-dark)" stroke-width="1.4"/></svg>info.veltahome@pec.example</li>
        <li><svg viewBox="0 0 12 12"><rect x="1" y="3" width="10" height="6" rx="2" fill="none" stroke="var(--navy-on-dark)" stroke-width="1.4"/></svg>K7RTZQ2</li>
      </ul>
    </div>
    <div class="back-panel" role="img" aria-label="Embossed brand decoration area"></div>
  </section>

  <section class="card card--front" aria-label="Business card front">
    <div class="brand brand--large"><span class="brand__mark"></span>VELTA HOME</div>
  </section>
</main>
</body>
</html>
```